Stationery Design Project for a consulting/educational company

We need a stationery design for a consulting / educational company called "VORN d.o.o.". We are an official partner (yet stand-alone company) of the TALMO Institute, Germany (www.talmo-example.de) that covers practically all themes regarding production optimisation, efectiveness, productivity (time studies, workplace organisation,...) We need the design for:

- a CERTIFICATE for seminar participates
- business cards
- letterhead

We are changing our webpage to their design, so we need to change the stationaries as well. I included 2 current logos, one with current color scheme (not important) and the other black/white with a frame. I also included the TALMO original certificate. Only the font + name"VORN" is important, the rest is up to you
Updates

Designs look good, but perhaps a gray & green combo would look nicer? Like on www.talmo-example.de? And without the frames?

Target Market(s)

Larger production companies top and middle management

Industry/Entity Type

Business

Requirements
Must have
• - the stationaries (all of them) should, besides the company name "VORN", also include the logo TALMO (in its color), like on their webpage www.talmo-example.de
Nice to have
• - certificate could use 5th color (e.g. silver) to make an impression
- similar color scheme to www.talmo-example.de

```html
<!DOCTYPE html>
<html lang="en">
<head>
<meta charset="utf-8">
<title>VORN d.o.o. – Stationery Design Project</title>
<link rel="stylesheet" href="https://fonts.googleapis.com/css2?family=Cinzel:wght@400;600&family=Cormorant+SC:wght@500;600&family=Didact+Gothic&display=swap">
<style>
  :root {
    --teal: #00b8ba;
    --teal-deep: #07b3b5;
    --teal-light: #62d8d8;
    --band-grey: #e3e3e3;
    --paper: #ffffff;
    --ink: #1d1d1d;
    --ink-soft: #7a7a7a;
    --mark-grey: #bdbdbd;
    --board-light: #ffffff;
    --board-edge: #d9d9d9;
    --bar: #000000;
  }
  * { margin: 0; padding: 0; box-sizing: border-box; }
  html, body { width: 1200px; height: 848px; overflow: hidden; }
  body {
    position: relative;
    background: radial-gradient(ellipse at 50% 45%, var(--board-light) 0%, #f1f1f1 55%, var(--board-edge) 100%);
    font-family: "Cormorant SC", "Times New Roman", serif;
  }

  .corner-ribbon { position: absolute; left: 0; top: 0; }

  /* ---------- Letterhead ---------- */
  .letterhead {
    position: absolute; left: 174px; top: 87px;
    width: 480px; height: 623px;
    background: var(--paper);
    box-shadow: 0 5px 10px rgba(0,0,0,.35);
  }
  .letterhead__header { position: absolute; left: 0; top: 0; width: 459px; height: 97px; }
  .letterhead__strip-top { position: absolute; left: 0; top: 0; width: 100%; height: 15px; background: var(--teal); }
  .letterhead__band-grey { position: absolute; left: 0; top: 15px; width: 100%; height: 39px; background: var(--band-grey); }
  .letterhead__band-teal { position: absolute; left: 0; top: 54px; width: 100%; height: 43px; background: var(--teal); }
  .letterhead__mark-strip {
    position: absolute; left: 421px; top: 0; width: 31px; height: 97px;
    background: var(--paper);
    display: flex; align-items: center; justify-content: center;
  }
  .brand-mark {
    font-family: "Cinzel", "Times New Roman", serif;
    font-weight: 600;
    color: var(--mark-grey);
    letter-spacing: 1px;
    white-space: nowrap;
  }
  .brand-mark--vertical { writing-mode: vertical-rl; transform: rotate(180deg); }
  .letterhead .brand-mark { font-size: 15px; }

  .letterhead__identity {
    position: absolute; right: 67px; top: 17px; text-align: right; color: var(--ink);
  }
  .company-name { font-family: "Cinzel", serif; font-size: 17px; line-height: 20px; letter-spacing: .3px; }
  .company-slogan { font-size: 8px; line-height: 10px; font-weight: 600; }
  .letterhead__contact {
    position: absolute; right: 67px; top: 54px; text-align: right;
    color: var(--paper); font-size: 8.5px; line-height: 8.6px; font-weight: 600; padding-top: 2px;
  }

  /* ---------- Business card front ---------- */
  .card { position: absolute; width: 320px; height: 191px; box-shadow: 0 4px 8px rgba(0,0,0,.4); overflow: hidden; }
  .card--front {
    left: 704px; top: 196px;
    background:
      radial-gradient(ellipse 55% 60% at 45% 10%, rgba(255,255,255,.35), rgba(255,255,255,0) 70%),
      linear-gradient(to bottom, var(--teal-light) 0%, #3fcbcc 52%, var(--teal) 52%, var(--teal-deep) 100%);
  }
  .card--front .card__mark-strip {
    position: absolute; left: 253px; top: 0; width: 43px; height: 100%;
    background: var(--paper);
    display: flex; align-items: flex-start; justify-content: center; padding-top: 18px;
  }
  .card--front .brand-mark { font-size: 26px; }
  .card--front .card__edge { position: absolute; left: 296px; top: 0; width: 24px; height: 100%; background: var(--teal); }

  /* ---------- Business card back ---------- */
  .card--back {
    left: 704px; top: 412px; height: 190px;
    background: linear-gradient(to bottom, #f7f7f7 0%, #dcdcdc 100%);
  }
  .card__art { position: absolute; left: 0; top: 0; }
  .card__holder { position: absolute; left: 23px; top: 48px; }
  .holder-name { font-family: "Cinzel", serif; font-size: 18px; color: #8a8a8a; letter-spacing: .5px; }
  .holder-title { font-size: 8.5px; color: var(--ink-soft); letter-spacing: 3.4px; margin-top: 3px; font-weight: 600; }
  .card__contact {
    position: absolute; left: 23px; top: 112px;
    font-size: 8px; line-height: 10.4px; color: var(--ink); font-weight: 600;
  }
  .card--back .brand-mark {
    position: absolute; left: 196px; top: 124px;
    font-size: 19px; transform: rotate(-38deg); transform-origin: left top;
  }

  /* ---------- Caption bar ---------- */
  .caption-bar {
    position: absolute; left: 0; top: 792px; width: 1200px; height: 56px; background: var(--bar);
  }
  .caption-bar__text {
    position: absolute; left: 62px; top: 18px;
    font-family: "Didact Gothic", Arial, sans-serif; font-size: 15px; color: #ffffff;
  }
</style>
</head>
<body>

<svg class="corner-ribbon" width="230" height="110" viewBox="0 0 230 110" aria-hidden="true">
  <polygon points="0,58 0,104 205,0 115,0" fill="var(--bar)"/>
</svg>

<section class="letterhead" aria-label="Letterhead">
  <div class="letterhead__header">
    <div class="letterhead__strip-top"></div>
    <div class="letterhead__band-grey"></div>
    <div class="letterhead__band-teal"></div>
    <div class="letterhead__identity">
      <p class="company-name">Company name</p>
      <p class="company-slogan">company slogan</p>
    </div>
    <div class="letterhead__contact">
      <p>company address</p>
      <p>Phone : 01234 567 89</p>
      <p>fax: 01234 567 89</p>
      <p>www.yourcompanynmae.com</p>
    </div>
    <div class="letterhead__mark-strip">
      <span class="brand-mark brand-mark--vertical">TALMO</span>
    </div>
  </div>
</section>

<section class="card card--front" aria-label="Business card, front">
  <div class="card__mark-strip">
    <span class="brand-mark brand-mark--vertical">TALMO</span>
  </div>
  <div class="card__edge"></div>
</section>

<section class="card card--back" aria-label="Business card, back">
  <svg class="card__art" width="320" height="190" viewBox="0 0 320 190" aria-hidden="true">
    <defs>
      <linearGradient id="teal-panel" x1="0" y1="0" x2="0" y2="1">
        <stop offset="0" stop-color="#19c4c5"/>
        <stop offset="1" stop-color="#00b3b5"/>
      </linearGradient>
    </defs>
    <polygon points="0,101 263,101 148,190 0,190" fill="url(#teal-panel)"/>
    <polygon points="263,101 320,101 320,131 191,190 148,190" fill="#ffffff"/>
    <polygon points="320,131 320,190 191,190" fill="url(#teal-panel)"/>
  </svg>
  <div class="card__holder">
    <p class="holder-name">John Doe</p>
    <p class="holder-title">your job title here</p>
  </div>
  <div class="card__contact">
    <p>company address</p>
    <p>Phone : 01234 567 89 | fax: 01234 567 89</p>
    <p>johndoe@companyname.com</p>
    <p>www.yourcompanynmae.com</p>
  </div>
  <span class="brand-mark">TALMO</span>
</section>

<footer class="caption-bar">
  <p class="caption-bar__text">Stationery Design Project for a consulting/educational company</p>
</footer>

</body>
</html>
```